依頼詳細
基本レイアウトについては
https://zuvaro.com/diagrams/7kq2m94T3XhpleWn
もしくは、添付データのワイヤーをご参照ください。

全体の雰囲気としては
http://www.morelid.co.jp/eco/forest/
のような和風・職人の雰囲気がありつつも、
あまり古臭くならないようなイメージを希望いたします。

色合いについては特に制限はないですが、上記を踏まえ
赤(エンジ)・オレンジ・紫・緑・ベージュなどが良いかと思います。

提出の写真素材があまり多くないのですが、
http://boxquiltry.jp/download/8fa27cd04b91e5a36d0c2bb7105e94f2d6a1c479
にアップロードしたものをご利用いただければ幸いです。

また、
http://vomre.jp/
などから、5000円程度までならこちらにて購入可能です。
カンプデータにて作成頂き、納品時に当方にて購入したデータに差し替えていただければと存じます。

【ロゴについて】
ロゴについては代表の家紋である
「剣片喰 (けんかたばみ)」を使用します。
添付データにjpgのデータを添付しております。
色合いについては、必ずしも黒である必要はないので、デザインに合わせて
ご調整いただいて結構です。

ページ数
1ページ
希望イメージ
シンプル 複雑
単色 カラフル
暗い 明るい
日常 高級
遊び心 厳粛
未来的 伝統的
女性的 男性的
希望する色
特に規定はないですが、和風をイメージを取り入れた色合いを希望します。
納品ファイル
• 高解像度JPG (.jpg)
• フォトショップ形式 (.psd)
補足説明
先方提出のイメージ写真については
下記URLからダウンロードしてご利用ください。

また、
http://vomre.jp/

【参考サイト】
hhttp://www.morelid.co.jp/eco/forest/
→全体の構成、誠実な印象とコンテンツの見やすさを気に入られています。
→色合いについては、必ずしもグリーンベースである必要はありません。

基本的には和風・職人の雰囲気を出すようなサイトが希望なのですが、
あまり和風すぎる、職人すぎる印象は出したくない要望がございます。
(代表自体が35歳と若いこと、マンションの緑地管理などを出していく希望があるため)

http://tokuvane.jp/
のような雰囲気だと、少し古臭すぎる印象がございます。

とはいえ
http://www.qrv-jp.com/
のような感じですと少しポップすぎる印象です

http://plinth-galore.com/2012/166.html
http://plinth-galore.com/2011/115.html
→フッター部分の参照
■ 選んだ理由

クライアントとの協議の結果、こちらの案を採用させて頂きました。
職人っぽい雰囲気でありつつ、今っぽい印象を残したデザインが
選考の決め手になりました。

■ 提案者全員のお礼・コメント

この度は多数ご提案いただきありがとうございました。
当選に至らなかったランサー様には大変心苦しいのですが、
次の機会がございましたら、是非ご提案頂ければ幸いです。
引続きよろしくお願いいたします。

```html
<!DOCTYPE html>
<html lang="ja">
<head>
<meta charset="UTF-8">
<title>緑葉園 | 植木屋・造園工事・外構工事</title>
<link href="https://fonts.googleapis.com/css2?family=Noto+Sans+JP:wght@400;700&family=Noto+Serif+JP:wght@500;700&display=swap" rel="stylesheet">
<style>
:root{
  --green-dark:#2c3622;
  --green:#4c6b2a;
  --green-btn:#3f5a22;
  --beige:#ebe5d4;
  --beige-line:#d6cdb6;
  --paper:#ffffff;
  --text:#3a3a32;
  --muted:#7a7565;
}
*{box-sizing:border-box;margin:0;padding:0}
html,body{width:889px;height:1200px;overflow:hidden}
body{font-family:"Noto Sans JP",sans-serif;color:var(--text);background:var(--beige);font-size:10px;line-height:1.5}
.wrap{width:720px;margin:0 auto;position:relative}

/* header */
.site-header{background:var(--paper);height:88px}
.site-header .wrap{height:88px}
.tagline{position:absolute;left:0;top:8px;font-size:8px;color:var(--muted)}
.brand{position:absolute;left:0;top:30px;display:flex;align-items:center;gap:8px}
.brand-mark{width:26px;height:26px;border-radius:50%;background:var(--green-dark)}
.brand-name{font-family:"Noto Serif JP",serif;font-weight:700;font-size:24px;color:var(--green-dark);letter-spacing:2px}
.header-contact{position:absolute;right:0;top:6px;text-align:right}
.btn{display:inline-block;background:var(--green-btn);color:#fff;font-size:9px;padding:5px 16px;font-weight:700}
.phone{font-family:"Noto Serif JP",serif;font-size:20px;font-weight:700;color:var(--green-dark);margin-top:8px;display:flex;align-items:center;gap:4px;justify-content:flex-end}
.phone svg{width:16px;height:16px}
.hours{font-size:7px;color:var(--muted)}

/* nav */
.global-nav{background:var(--green-dark);height:22px}
.global-nav ul{list-style:none;display:flex;width:720px;margin:0 auto;height:22px}
.global-nav li{flex:1;color:#e7e2d0;font-size:9px;text-align:center;line-height:22px;border-left:1px solid #46503a}
.global-nav li:last-child{border-right:1px solid #46503a}

/* hero */
.hero{height:218px;background:linear-gradient(180deg,#5d6e3c 0%,#7c8f4d 35%,#56693a 70%,#3b4a2a 100%)}

/* body */
.content{display:flex;gap:15px;padding-top:22px}
.sidebar{width:236px}
.main{width:469px}

.banner-green{height:68px;background:linear-gradient(90deg,#3a4a2a,#5c7037);display:flex;align-items:center;padding-left:14px;color:#fff;font-family:"Noto Serif JP",serif;font-weight:700;font-size:12px;line-height:1.4}
.contact-box{background:var(--paper);margin-top:14px;border:1px solid var(--beige-line);text-align:center;padding-bottom:10px}
.contact-box h3{background:var(--green-dark);color:#fff;font-size:10px;padding:6px 0}
.contact-box .phone{justify-content:center;font-size:20px;margin:12px 0 8px}
.contact-box .btn{width:200px;padding:7px 0}
.contact-box .addr{margin:10px 14px 0;padding:6px;border:1px solid var(--beige-line);font-size:8px;color:var(--muted)}
.side-nav{list-style:none;margin-top:10px;background:var(--paper);border:1px solid var(--beige-line)}
.side-nav li{height:30px;display:flex;align-items:center;gap:8px;padding-left:12px;font-size:9.5px;border-bottom:1px dotted var(--beige-line)}
.side-nav li:last-child{border-bottom:none}
.side-nav li::before{content:"";width:12px;height:12px;border-radius:50%;background:var(--green)}

.intro{background:var(--paper);height:200px;position:relative;border:1px solid var(--beige-line)}
.intro-text{position:absolute;left:16px;top:16px;width:250px}
.intro-text h2{font-family:"Noto Serif JP",serif;font-size:12.5px;font-weight:700;color:var(--green-dark);line-height:1.6}
.intro-text p{margin-top:8px;font-size:7.5px;color:var(--muted);line-height:1.7}
.intro-photo{position:absolute;right:10px;top:10px;width:185px;height:132px;background:linear-gradient(135deg,#9a8b6c,#6d6a4a 55%,#4f5d35)}
.intro-tag{position:absolute;left:16px;top:126px;background:var(--green);color:#fff;font-size:8px;padding:3px 10px}
.service-strip{position:absolute;left:0;right:0;bottom:0;height:40px;background:var(--green-dark);display:flex;align-items:center;justify-content:center;gap:10px;color:#e5dfc9;font-size:8px}

.section{display:flex;margin-top:12px}
.section-title{width:40px;font-family:"Noto Serif JP",serif;font-weight:700;font-size:15px;color:var(--green-dark);writing-mode:vertical-rl;letter-spacing:4px;padding-top:4px}
.section-body{flex:1}
.news{list-style:none;background:var(--paper);border:1px solid var(--beige-line)}
.news li{height:25px;display:flex;align-items:center;border-bottom:1px dotted var(--beige-line);font-size:8px;padding:0 10px}
.news li:last-child{border-bottom:none}
.news time{color:var(--green);width:70px}
.cases{display:grid;grid-template-columns:1fr 1fr;gap:10px}
.case{height:110px}
.case-a{background:linear-gradient(180deg,#a9b4c0,#8a6d4b)}
.case-b{background:linear-gradient(180deg,#6f7f4a,#a4947a)}
.case-c{background:linear-gradient(180deg,#b89a6c,#8d7452)}
.case-d{background:linear-gradient(180deg,#c7b48e,#9f8c6d)}

/* footer */
.site-footer{position:absolute;left:0;top:1032px;width:889px;height:138px;background:var(--green-dark);color:#ddd7c3}
.site-footer .wrap{height:138px}
.footer-brand{position:absolute;left:0;top:14px}
.footer-brand .tagline{position:static;color:#b8b29f}
.footer-brand .brand{position:static;margin-top:6px}
.footer-brand .brand-mark{background:#ddd7c3}
.footer-brand .brand-name{color:#fff;font-size:20px}
.footer-brand .addr{margin-top:8px;font-size:7.5px;color:#b8b29f}
.footer-links{position:absolute;left:240px;top:16px;display:grid;grid-template-columns:repeat(4,118px);row-gap:6px;list-style:none;font-size:8px}
.footer-links li::before{content:"▶ ";font-size:6px;color:#9aab6a}
.footer-contact{position:absolute;left:240px;top:84px;right:0;display:flex;align-items:center;gap:16px;border-top:1px solid #46503a;padding-top:12px}
.footer-contact .label{font-size:9px;font-weight:700;color:#fff}
.footer-contact .phone{margin:0;color:#fff}
.footer-contact .btn{background:#5b7a31;padding:7px 28px}
.copyright{position:absolute;left:0;top:1170px;width:889px;height:30px;background:#1f261a;color:#a7a18d;font-size:7.5px;text-align:center;line-height:30px}
</style>
</head>
<body>
<header class="site-header">
  <div class="wrap">
    <p class="tagline">お庭づくりの匠 | 心をこめて手掛けます</p>
    <div class="brand"><span class="brand-mark"></span><span class="brand-name">緑葉園</span></div>
    <div class="header-contact">
      <a class="btn">お問い合わせフォーム</a>
      <div class="phone"><svg viewBox="0 0 24 24"><path fill="#2c3622" d="M6.6 10.8a15 15 0 0 0 6.6 6.6l2.2-2.2c.3-.3.7-.4 1-.2 1.1.4 2.3.6 3.6.6.6 0 1 .4 1 1V20c0 .6-.4 1-1 1A17 17 0 0 1 3 4c0-.6.4-1 1-1h3.5c.6 0 1 .4 1 1 0 1.3.2 2.5.6 3.6.1.3 0 .7-.2 1z"/></svg>(0120)-418-962</div>
      <p class="hours">受付時間 9:00〜18:00 日曜・祝日定休</p>
    </div>
  </div>
</header>
<nav class="global-nav">
  <ul><li>トップページ</li><li>樹木剪定作業</li><li>植栽・外構工事</li><li>マンション緑地管理</li><li>施工事例</li><li>よくある質問</li><li>会社案内</li></ul>
</nav>
<div class="hero" role="img" aria-label="手入れされた生垣と芝生の写真"></div>

<div class="wrap content">
  <aside class="sidebar">
    <div class="banner-green" role="img" aria-label="マンション緑地の写真を背景にした案内バナー">マンション緑地<br>管理のご案内</div>
    <div class="contact-box">
      <h3>お問い合わせ・資料請求</h3>
      <div class="phone"><svg viewBox="0 0 24 24"><path fill="#2c3622" d="M6.6 10.8a15 15 0 0 0 6.6 6.6l2.2-2.2c.3-.3.7-.4 1-.2 1.1.4 2.3.6 3.6.6.6 0 1 .4 1 1V20c0 .6-.4 1-1 1A17 17 0 0 1 3 4c0-.6.4-1 1-1h3.5c.6 0 1 .4 1 1 0 1.3.2 2.5.6 3.6.1.3 0 .7-.2 1z"/></svg>(0120)-418-962</div>
      <a class="btn">お問い合わせフォーム</a>
      <p class="addr">〒210-0000<br>緑ヶ丘市若葉区若葉町1-2-3</p>
    </div>
    <ul class="side-nav">
      <li>トップページ</li><li>樹木剪定作業</li><li>植栽・外構工事</li><li>マンション緑地管理</li><li>施工事例</li><li>よくある質問</li><li>会社案内</li><li>お問い合わせ</li>
    </ul>
  </aside>

  <main class="main">
    <section class="intro">
      <div class="intro-text">
        <h2>緑ヶ丘市若葉区の<br>植木屋・造園工事・外構工事は<br>緑葉園にお任せ下さい。</h2>
        <p>お庭の手入れから造園工事まで、職人が丁寧に対応いたします。マンションの緑地管理もお気軽にご相談下さい。</p>
      </div>
      <span class="intro-tag">お見積り無料</span>
      <div class="intro-photo" role="img" aria-label="剪定作業をする職人の写真"></div>
      <div class="service-strip"><span>樹木剪定・グリーンケア</span><span>植栽・造園工事</span><span>フェンス工事</span><span>ウッドデッキ</span><span>緑地管理</span></div>
    </section>

    <section class="section">
      <h2 class="section-title">お知らせ</h2>
      <div class="section-body">
        <ul class="news">
          <li><time>2013/10/01</time>ホームページをリニューアルいたしました。</li>
          <li><time>2013/09/20</time>秋の剪定のご予約を受け付けております。</li>
          <li><time>2013/09/05</time>施工事例に新しい写真を追加しました。</li>
          <li><time>2013/08/22</time>夏季休業のお知らせを掲載しました。</li>
          <li><time>2013/08/01</time>マンション緑地管理の案内を更新しました。</li>
          <li><time>2013/07/15</time>外構工事のご相談を受け付けております。</li>
        </ul>
      </div>
    </section>

    <section class="section">
      <h2 class="section-title">施工事例</h2>
      <div class="section-body cases">
        <div class="case case-a" role="img" aria-label="レンガの花壇と外構の施工写真"></div>
        <div class="case case-b" role="img" aria-label="庭木と石畳の施工写真"></div>
        <div class="case case-c" role="img" aria-label="木製フェンスの施工写真"></div>
        <div class="case case-d" role="img" aria-label="目隠しフェンスの施工写真"></div>
      </div>
    </section>
  </main>
</div>

<footer class="site-footer">
  <div class="wrap">
    <div class="footer-brand">
      <p class="tagline">お庭づくりの匠 | 心をこめて手掛けます</p>
      <div class="brand"><span class="brand-mark"></span><span class="brand-name">緑葉園</span></div>
      <p class="addr">〒210-0000<br>緑ヶ丘市若葉区若葉町1-2-3<br>TEL 045-731-2286</p>
    </div>
    <ul class="footer-links">
      <li>トップページ</li><li>植栽・外構工事</li><li>施工事例</li><li>サイトマップ</li>
      <li>樹木剪定作業</li><li>マンション緑地管理</li><li>よくある質問</li><li>プライバシーポリシー</li>
      <li>会社案内</li><li>お問い合わせ</li>
    </ul>
    <div class="footer-contact">
      <span class="label">お問い合わせ・資料請求<br>はこちらから</span>
      <div class="phone">(0120)-418-962</div>
      <a class="btn">お問い合わせフォーム</a>
    </div>
  </div>
</footer>
<p class="copyright">Copyright © 緑葉園 All Rights Reserved.</p>
</body>
</html>
```